Tallow Salmon Labels

We need a graphic design label for a new product launch. Tallow is an 100% Australian family business specialised in making marinades made from natural and locally sourced fresh ingredients for fish and seafood. We make remarkable food for fine cooking prepared by hand at our kitchen in Condell Park, using the same ingredients and techniques you would use at home.

We are planning to launch three marinades for salmon.
The flavours are:

- Herb, Lemon & Cracked Black Pepper
- Ginger, Honey & Soy
- Coriander, Lemongrass, Shallot and Ginger

The marinades will be packed in a 300 grams clear pouch with spout and sold in the seafood section of a major retail supermarket.

Measurements of the pouch: 140 mm wide and 210 mm high but only 160 mm high from the spout downwards.

Label: For the label, It will be a 120mm wide X 120mm high If not slightly smaller. Please refer to File 2: to see the pouch.

The label will cover 75% of the front of the pouch and the marinade itself will be visible in the remaining 25 % of the pouch. The colours of the marinades are green for Herb, Lemon & Cracked Black Pepper and Coriander, Lemongrass, Shallot and Ginger; and dark brown for Ginger, Honey & Soy.

Our marinades do not contain additives. The marinades are Gluten free.

The label needs to visually communicate that the marinade is used for salmon.

Please choose a suitable typography for our name Tallow that communicates an artisan feel.

Please refer to File 1 as a guide to what we would like, but keep in mind we are very open to any ideas you may have.

Colours should reflect the nature of our business, as outlined above.
Updates

Hello Designers,

This is what the actual pouch looks like https://www.filecrate-example.net/sc/4kd9w2m7x1/Qa81Lpt3z_

We would like the label to be roughly 120mm X 120mm or within those parameters to fit the packaging.

Thank you!
- Moira

Hey Designers,

we have been looking at your designs and while we have liked some elements of them we would like to see more creativity with the actual graphics and shapes of the labels, different colour contrast and more clever and quirky designs. We want to make fish fun and interesting to consumers, something rustic that catches the eye but at the same time is still sophisticated and upmarket. 

We would like to see the following on your packaging designs:

- Pastels colours (green, blue and yellow).
- The 'Tallow gourmet' font to be in bolder typography
- An ink looking stamp for 'gluten free, no additives'
- Something about the product being hand crafted
- Must include the following text: Marinades made from natural and locally sourced fresh ingredients for fish and seafood

here are some examples for you to be inspired by

Some font ideas ..

http://pinboardly-example.net/pin/518203947716250341/
http://pinboardly-example.net/pin/73915268401837762/
http://pinboardly-example.net/pin/629450183027741856/
http://pinboardly-example.net/pin/384720615099214730/
http://pinboardly-example.net/pin/957301846620387412/
http://pinboardly-example.net/pin/140862397785023561/

colours/images/graphics

http://pinboardly-example.net/pin/803174529936610248/
http://pinboardly-example.net/pin/471028395512846307/
http://pinboardly-example.net/pin/695283017740158236/
http://pinboardly-example.net/pin/332610847958271649/ (We like this concept) 

Good luck! 

 

Target Market(s)

Home cooks, young professionals, anyone with a healthy eating lifestyle.

Industry/Entity Type

Graphic Design

Requirements
Must have
• The label needs to visually communicate that the marinade is used for salmon.
- Include "Gluten Free" and "No Additives" on the label
- Outline the freshness of the ingredients used in the marinade eg. Coriander, Lemongrass, Shallot and Ginger to be included on the label.
- Bright and eye catching colours (food friendly colours).
Nice to have
• - Open to pastel colours
- Vector drawings
Should not have
• - dull colours

```html
<!DOCTYPE html>
<html lang="en">
<head>
<meta charset="utf-8">
<title>Tallow Salmon Marinade Label</title>
<link rel="stylesheet" href="https://fonts.googleapis.com/css2?family=Oswald:wght@400&family=Federo&family=Parisienne&family=Raleway:wght@300&display=swap">
<style>
  :root {
    --page: #ffffff;
    --label-green: #8dc63f;
    --frame-red: #ec2227;
    --brand-blue: #2b3990;
    --accent-yellow: #f5e63b;
    --text-white: #ffffff;
    --fish-red: #e8262b;
  }
  html, body {
    margin: 0;
    padding: 0;
    width: 1200px;
    height: 1200px;
    overflow: hidden;
    background: var(--page);
  }
  .canvas {
    position: relative;
    width: 1200px;
    height: 1200px;
    background: var(--page);
  }
  .label {
    position: absolute;
    left: 93px;
    top: 98px;
    width: 1020px;
    height: 1020px;
    background: var(--label-green);
  }
  .frame {
    position: absolute;
    left: 0;
    top: 0;
    width: 1200px;
    height: 1200px;
  }
  .brand-name {
    position: absolute;
    left: 0;
    width: 1200px;
    top: 348px;
    margin: 0;
    text-align: center;
    font-family: "Oswald", sans-serif;
    font-weight: 400;
    font-size: 138px;
    line-height: 1;
    letter-spacing: 2px;
    color: var(--brand-blue);
  }
  .product-name {
    position: absolute;
    left: 0;
    width: 1200px;
    top: 520px;
    margin: 0;
    text-align: center;
    font-family: "Federo", sans-serif;
    font-weight: 400;
    font-size: 70px;
    line-height: 1;
    letter-spacing: 3px;
    color: var(--accent-yellow);
  }
  .flavour {
    position: absolute;
    left: 0;
    width: 1200px;
    top: 602px;
    margin: 0;
    text-align: center;
    font-family: "Parisienne", cursive;
    font-size: 40px;
    line-height: 1;
    color: var(--text-white);
  }
  .fish-art {
    position: absolute;
    left: 327px;
    top: 684px;
    width: 552px;
    height: 178px;
  }
  .claims {
    position: absolute;
    left: 222px;
    top: 918px;
    margin: 0;
    padding: 0;
    list-style: none;
    font-family: "Raleway", sans-serif;
    font-weight: 300;
    font-size: 25px;
    color: var(--accent-yellow);
  }
  .claims li {
    display: flex;
    align-items: center;
    height: 48px;
  }
  .claims svg {
    width: 26px;
    height: 26px;
    margin-right: 12px;
  }
  .freshness {
    position: absolute;
    left: 780px;
    top: 950px;
    margin: 0;
    font-family: "Federo", sans-serif;
    font-size: 62px;
    line-height: 1;
    letter-spacing: 2px;
    color: var(--text-white);
  }
</style>
</head>
<body>
<main class="canvas">
  <div class="label"></div>

  <svg class="frame" viewBox="0 0 1200 1200" aria-hidden="true">
    <g fill="none" stroke="var(--frame-red)" stroke-width="8" stroke-linecap="round">
      <path d="M 128 146 Q 600 128 1074 146"/>
      <path d="M 128 1032 Q 600 1050 1074 1034"/>
      <path d="M 158 146 Q 140 590 156 1032"/>
      <path d="M 1046 146 Q 1064 590 1046 1034"/>
      <circle cx="128" cy="146" r="27"/>
      <circle cx="1074" cy="146" r="27"/>
      <circle cx="128" cy="1032" r="27"/>
      <circle cx="1074" cy="1034" r="27"/>
    </g>
  </svg>

  <h1 class="brand-name">TALLOW</h1>
  <h2 class="product-name">salmon marinade</h2>
  <p class="flavour">Coriander, Lemongrass, Shallot and Ginger</p>

  <svg class="fish-art" viewBox="0 0 552 178" role="img" aria-label="Textured red salmon illustration">
    <rect x="0" y="20" width="552" height="140" rx="70" fill="var(--fish-red)"/>
  </svg>

  <ul class="claims">
    <li>
      <svg viewBox="0 0 26 26" aria-hidden="true"><path d="M3 15 L9 22 L23 4" fill="none" stroke="var(--accent-yellow)" stroke-width="3" stroke-linecap="round" stroke-linejoin="round"/></svg>
      Gluten Free
    </li>
    <li>
      <svg viewBox="0 0 26 26" aria-hidden="true"><path d="M3 15 L9 22 L23 4" fill="none" stroke="var(--accent-yellow)" stroke-width="3" stroke-linecap="round" stroke-linejoin="round"/></svg>
      No Additives
    </li>
  </ul>

  <p class="freshness">fresh</p>
</main>
</body>
</html>
```